WE RISE NOW - Personal Growth Seminar

The project is collaboration between Desmond Farrow and Marian Pelloway. It will combine the skills of both parties to launch an inspirational and motivation Personal Growth Seminar. We are looking for an e-flyer and a general design that we can use in our promotional work

The programme is a one day seminar which will show delegates how to

1) Kick start your life
2) Overcome obstacles and self sabotage
3) Take control of your future
4) Think bigger than you thought possible
5) Increase your confidence and self belief
6) Six steps to WE RISE NOW success

Our values for the seminar, that the eflyer should represent are:
Professional
Freedom
Nature (really important theme)
Fun
Honest
Balance
Integrity

We want to GRAB people's attention and then ENGAGE them into booking onto the seminar. We will send over details for the links to the seminar and phone numbers etc later, so they need to be incorporated. The seminar will be held in a hotel called The Hazelmere (nature and growth theme)

The one thing to remember is, to step back from the design and ask yourself would you book the seminar, based on what you see.

Our websites so you can see our current themes are www.marianpelloway.com and www.desmondfarrow.co.uk

Target Market(s)

Adults based in UK, between 25 and 50 years of age.

Industry/Entity Type

Hotel

Requirements
Must have
• Nature theme - growth
Fun but professional

Colours green but more vibrant like grass colour, nothing dull or washed out

Nice to have
• The picture will give you an idea but doesn't need to be used, it is just for guidance.

A Tree theme could be used - perhaps with the WE RISE NOW on the branches
Should not have
• Should not include cartoons

Gawdy colours or too much text

```html
<!DOCTYPE html>
<html lang="en">
<head>
<meta charset="utf-8">
<title>We Rise Now – One Day Seminar</title>
<link href="https://fonts.googleapis.com/css2?family=Arimo:wght@400;700&family=Cormorant+Garamond:wght@500;600&display=swap" rel="stylesheet">
<style>
  :root {
    --grass-deep: #1f6b0f;
    --grass-mid: #3c9a16;
    --grass-bright: #7fd02a;
    --grass-light: #b8ec6a;
    --panel-white: #ffffff;
    --ink-dark: #27361f;
    --ink-body: #2c2c2c;
    --title-silver: #e9ece6;
    --title-shadow: rgba(20, 50, 10, 0.55);
    --dot-green: #9be24a;
  }
  * { margin: 0; padding: 0; box-sizing: border-box; }
  html, body { width: 849px; height: 1200px; overflow: hidden; background: #fff; }
  .flyer {
    position: relative;
    width: 849px;
    height: 1200px;
    overflow: hidden;
    font-family: "Arimo", Arial, sans-serif;
  }
  .grass-background {
    position: absolute; inset: 0;
    background:
      radial-gradient(ellipse 60% 25% at 70% 8%, var(--grass-light) 0%, transparent 70%),
      radial-gradient(ellipse 50% 20% at 20% 35%, var(--grass-bright) 0%, transparent 70%),
      radial-gradient(ellipse 70% 12% at 50% 97%, var(--grass-light) 0%, transparent 70%),
      linear-gradient(180deg, var(--grass-mid) 0%, var(--grass-deep) 30%, var(--grass-mid) 55%, var(--grass-deep) 80%, var(--grass-mid) 100%);
  }
  .panel-shape { position: absolute; inset: 0; }
  .headline {
    position: absolute; left: 0; width: 849px; text-align: center;
    font-family: "Cormorant Garamond", Georgia, serif;
    color: var(--title-silver);
    text-transform: lowercase;
    text-shadow: 3px 5px 4px var(--title-shadow);
  }
  .headline-main { top: 38px; font-size: 132px; font-weight: 600; line-height: 1; letter-spacing: 2px; }
  .headline-sub { top: 212px; font-size: 78px; font-weight: 500; line-height: 1; }
  .headline-echo {
    top: 268px; font-size: 78px; font-weight: 500; line-height: 1;
    color: rgba(20, 60, 10, 0.35); text-shadow: none; transform: scaleY(-0.5); transform-origin: top;
  }
  .intro {
    position: absolute; left: 39px; top: 470px; width: 520px;
    color: #fff; font-size: 35px; line-height: 44px; font-weight: 400;
  }
  .benefits {
    position: absolute; left: 39px; top: 622px; list-style: none;
    color: #fff; font-weight: 700; font-size: 19px;
  }
  .benefits li { height: 40.5px; padding-left: 25px; position: relative; }
  .benefits li::before { content: "•"; position: absolute; left: 0; }
  .inline-brand {
    font-family: "Cormorant Garamond", Georgia, serif; font-weight: 600;
    font-size: 28px; text-transform: lowercase;
  }
  .venue-label {
    position: absolute; left: 39px; top: 874px;
    color: var(--ink-dark); font-weight: 700; font-size: 20px;
  }
  .venue-name {
    position: absolute; left: 30px; top: 895px;
    font-family: "Cormorant Garamond", Georgia, serif; font-weight: 600;
    font-size: 60px; color: var(--ink-dark); text-transform: lowercase; line-height: 1;
  }
  .venue-address {
    position: absolute; left: 39px; top: 976px;
    color: var(--ink-dark); font-weight: 700; font-size: 15px;
  }
  .event-date {
    position: absolute; left: 39px; top: 1001px;
    color: #fff; font-weight: 700; font-size: 22px; letter-spacing: 0.5px;
  }
  .event-date .sep { color: var(--dot-green); }
  .speaker { position: absolute; color: var(--ink-body); }
  .speaker-photo {
    position: absolute; width: 130px; height: 130px; border-radius: 50%;
    border: 4px solid #fff; box-shadow: 0 3px 8px rgba(0,0,0,0.45);
  }
  .speaker-name { position: absolute; font-size: 21px; white-space: nowrap; }
  .speaker-role { position: absolute; font-size: 16px; line-height: 22.5px; }
  .photo-one { left: 646px; top: 399px; background: radial-gradient(circle at 50% 45%, #d9a78a 0%, #8b5a40 55%, #2a2a2a 100%); }
  .photo-two { left: 629px; top: 672px; background: radial-gradient(circle at 50% 45%, #e8cbb6 0%, #b9a79b 50%, #d9dcd7 100%); }
  .name-one { left: 596px; top: 548px; }
  .role-one { left: 596px; top: 576px; width: 240px; }
  .name-two { left: 660px; top: 847px; }
  .role-two { left: 660px; top: 874px; width: 180px; }
  .websites {
    position: absolute; left: 0; width: 849px; top: 1110px; text-align: center;
    color: #fff; font-weight: 700; font-size: 28px; line-height: 36px;
    text-shadow: 2px 2px 3px rgba(0,0,0,0.55);
  }
</style>
</head>
<body>
<div class="flyer">
  <div class="grass-background" role="img" aria-label="Close-up photograph of bright green grass with dew drops"></div>

  <svg class="panel-shape" width="849" height="1200" viewBox="0 0 849 1200" aria-hidden="true">
    <path d="M380 462 C520 420 690 385 849 368 L849 1092 C760 1100 650 1115 578 1135 C592 980 588 640 570 468 Z" fill="var(--panel-white)"/>
    <path d="M0 430 C180 470 330 470 420 448 C560 410 700 385 849 362" fill="none" stroke="var(--grass-light)" stroke-width="3" opacity="0.7"/>
    <path d="M0 1120 C200 1150 420 1150 578 1132 C680 1115 770 1100 849 1095" fill="none" stroke="var(--grass-light)" stroke-width="3" opacity="0.7"/>
  </svg>

  <h1 class="headline headline-main">we rise now</h1>
  <p class="headline headline-sub">one day seminar</p>
  <p class="headline headline-echo" aria-hidden="true">one day seminar</p>

  <p class="intro">The programme is a one day seminar which will show delegates how to:-</p>

  <ul class="benefits">
    <li>Kick start your life</li>
    <li>Overcome obstacles and self sabotage</li>
    <li>Take control of your future</li>
    <li>Think bigger than you thought possible</li>
    <li>Increase your confidence and self belief</li>
    <li>Six steps to <span class="inline-brand">we rise now</span> success</li>
  </ul>

  <p class="venue-label">The Seminar is to be held at</p>
  <p class="venue-name">the hazelmere hotel</p>
  <p class="venue-address">First line of the Address • Street Name • Area • Post code</p>
  <p class="event-date">On Saturday <span class="sep">•</span> 00th <span class="sep">•</span> Month <span class="sep">•</span> 2011</p>

  <div class="speaker">
    <div class="speaker-photo photo-one" role="img" aria-label="Portrait photograph of speaker Desmond Farrow"></div>
    <p class="speaker-name name-one">Desmond Farrow</p>
    <p class="speaker-role role-one">Motivational speaker,<br>professional speaker,<br>inspirational speaker.</p>
  </div>

  <div class="speaker">
    <div class="speaker-photo photo-two" role="img" aria-label="Portrait photograph of speaker Marian Pelloway"></div>
    <p class="speaker-name name-two">Marian Pelloway</p>
    <p class="speaker-role role-two">Change Speaker,<br>Communication<br>Coach and<br>Hypnotherapist.</p>
  </div>

  <p class="websites">Visit our websites www.marianpelloway.com<br>and www.desmondfarrow.co.uk</p>
</div>
</body>
</html>
```